Business Card Design Project

Fernwick Pediatric Dentistry is a, kids dental office, located in prestigious Georgetown Washington DC, just blocks from the copper hall. We are fee for service office that has great patients who value their dental care.

I have attached our logo files in black and white, we would like our logo on our cards as well.

```html
<!DOCTYPE html>
<html lang="en">
<head>
<meta charset="utf-8">
<title>Fernwick Pediatric Dentistry – Business Card</title>
<link href="https://fonts.googleapis.com/css2?family=Cinzel:wght@400&family=Open+Sans:wght@400&display=swap" rel="stylesheet">
<style>
  :root {
    --stage: #4a4849;
    --ink: #0b0b0b;
    --paper: #ffffff;
    --text: #1a1a1a;
  }
  * { margin: 0; padding: 0; box-sizing: border-box; }
  html, body { width: 1200px; height: 858px; overflow: hidden; background: var(--stage); }
  .canvas { position: relative; width: 1200px; height: 858px; }

  .card {
    position: absolute;
    width: 560px;
    height: 320px;
    overflow: hidden;
  }
  .card--back { left: 80px; top: 90px; background: var(--ink); }
  .card--front { left: 560px; top: 448px; background: var(--paper); }

  .lockup {
    position: absolute;
    font-family: "Cinzel", serif;
    font-weight: 400;
    text-align: center;
    line-height: 1;
  }
  .lockup__rule { height: 1px; }
  .lockup__name { letter-spacing: 1px; }
  .lockup__sub { letter-spacing: 1px; }
  .lockup__est { letter-spacing: 1px; }

  .card--back .lockup { left: 50%; top: 118px; transform: translateX(-50%); width: 280px; color: var(--paper); }
  .card--back .lockup__rule { background: var(--paper); }
  .card--back .lockup__name { font-size: 38px; margin: 10px 0 4px; }
  .card--back .lockup__sub { font-size: 15px; }
  .card--back .lockup__est { font-size: 10px; margin: 4px 0 8px; }

  .card--front .lockup { right: 34px; top: 30px; width: 190px; color: var(--ink); }
  .card--front .lockup__rule { background: var(--ink); }
  .card--front .lockup__name { font-size: 26px; margin: 6px 0 3px; }
  .card--front .lockup__sub { font-size: 10.5px; }
  .card--front .lockup__est { font-size: 7px; margin: 3px 0 6px; }

  .person { position: absolute; left: 40px; top: 118px; color: var(--text); }
  .person__name { font-family: "Cinzel", serif; font-weight: 400; font-size: 26px; letter-spacing: 0.5px; }
  .person__role { font-family: "Open Sans", sans-serif; font-size: 14px; margin-top: 2px; }

  .address {
    position: absolute; left: 40px; top: 196px;
    font-family: "Open Sans", sans-serif; font-size: 14px; line-height: 1.35; color: var(--text);
    font-style: normal;
  }
  .contacts {
    position: absolute; left: 40px; top: 246px; list-style: none;
    font-family: "Open Sans", sans-serif; font-size: 13.5px; color: var(--text);
  }
  .contacts li { display: flex; align-items: center; gap: 10px; height: 19px; }
  .contacts svg { width: 12px; height: 12px; fill: var(--ink); flex: none; }

  .card__band { position: absolute; left: 0; right: 0; bottom: 0; height: 12px; background: var(--ink); }
</style>
</head>
<body>
<main class="canvas">

  <section class="card card--back" aria-label="Card back">
    <div class="lockup">
      <div class="lockup__rule"></div>
      <div class="lockup__name">Fernwick</div>
      <div class="lockup__sub">Pediatric Dentistry</div>
      <div class="lockup__est">Est. 2018</div>
      <div class="lockup__rule"></div>
    </div>
  </section>

  <section class="card card--front" aria-label="Card front">
    <div class="lockup">
      <div class="lockup__rule"></div>
      <div class="lockup__name">Fernwick</div>
      <div class="lockup__sub">Pediatric Dentistry</div>
      <div class="lockup__est">Est. 2018</div>
      <div class="lockup__rule"></div>
    </div>

    <div class="person">
      <h1 class="person__name">Daniel Harlow</h1>
      <p class="person__role">Founder &amp; CEO</p>
    </div>

    <address class="address">
      Suite 214, 18 Linden Row<br>
      Georgetown Washington DC
    </address>

    <ul class="contacts">
      <li>
        <svg viewBox="0 0 24 24" aria-hidden="true"><path d="M6.6 10.8a15.1 15.1 0 0 0 6.6 6.6l2.2-2.2a1 1 0 0 1 1-.25 11.4 11.4 0 0 0 3.6.57 1 1 0 0 1 1 1V20a1 1 0 0 1-1 1A17 17 0 0 1 3 4a1 1 0 0 1 1-1h3.5a1 1 0 0 1 1 1c0 1.25.2 2.45.57 3.57a1 1 0 0 1-.25 1z"/></svg>
        202 555 0148
      </li>
      <li>
        <svg viewBox="0 0 24 24" aria-hidden="true"><path d="M2 5h20v14H2z M2 5l10 8 10-8" /></svg>
        info@fernwickdental.com
      </li>
      <li>
        <svg viewBox="0 0 24 24" aria-hidden="true"><circle cx="12" cy="12" r="10"/><path d="M2 12h20M12 2c3 3 3 17 0 20M12 2c-3 3-3 17 0 20" stroke="#fff" stroke-width="1.4" fill="none"/></svg>
        www.fernwickdental.com
      </li>
    </ul>

    <div class="card__band"></div>
  </section>

</main>
</body>
</html>
```